Business Card Design for general contractor or developer

General Contractors. We build new buildings as well as redesign and/or remodel existing buildings. Mostly residential, but we want to expand to commercial as well, so we want the design not to be residential specific.We want the design to be modern, but necessarily minimalistic. A monogram type is also a consideration, but would like to see all ideas.

Target Market(s)

Real estate investors, homeowners, future homeowners, commercial building owners

Industry/Entity Type

Contractor

Contact Information for Business Card

BRIMCOVE Developers Corp, 2917 NE 88th Avenue Suite 412 Coral Springs, FL 33071, Darren Kopec, (305) 555-0148, darren@brimcovedev.example

Font styles to use
Other font styles liked:
• Modern type font

Requirements
Must have
• Must be modern looking
Nice to have
• Metallic type or a standout feature
Should not have
• Tools, floorplans

```html
<!DOCTYPE html>
<html lang="en">
<head>
<meta charset="utf-8">
<title>BRIMCOVE Developers Corp – Business Card</title>
<link href="https://fonts.googleapis.com/css2?family=Cabin:wght@400;700&family=Cinzel:wght@400&display=swap" rel="stylesheet">
<style>
  :root {
    --page-bg: #e9e7e3;
    --card-white: #ffffff;
    --brand-blue: #1f5fb4;
    --brand-blue-deep: #1a3f9c;
    --brand-blue-light: #2f8fd0;
    --text-grey: #4a4a4a;
    --text-dark: #1e1e1e;
    --ring-grey: #9a9a9a;
  }
  * { margin: 0; padding: 0; box-sizing: border-box; }
  html, body { width: 1200px; height: 885px; overflow: hidden; }
  body {
    background: var(--page-bg);
    font-family: "Cabin", sans-serif;
    position: relative;
  }
  .card {
    position: absolute;
    top: 288px;
    width: 540px;
    height: 309px;
    border-radius: 4px;
    overflow: hidden;
    box-shadow: 0 10px 28px rgba(0,0,0,0.18);
  }
  /* Front */
  .card-front { left: 40px; background: var(--card-white); }
  .front-circle { position: absolute; left: 0; top: 0; }
  .front-brand {
    position: absolute;
    left: 36px;
    bottom: 26px;
    width: 170px;
    font-size: 12px;
    font-weight: 700;
    line-height: 1.35;
    letter-spacing: 1.5px;
    color: var(--card-white);
    text-transform: uppercase;
    white-space: nowrap;
  }
  .front-details {
    position: absolute;
    left: 262px;
    top: 46px;
    width: 260px;
  }
  .person-name {
    font-size: 26px;
    font-weight: 700;
    letter-spacing: 2px;
    color: var(--brand-blue);
    text-transform: uppercase;
    line-height: 1;
  }
  .person-title {
    font-size: 14px;
    letter-spacing: 2px;
    color: var(--text-grey);
    margin-top: 4px;
  }
  .address {
    margin-top: 34px;
    font-size: 13.5px;
    line-height: 1.35;
    color: var(--text-dark);
  }
  .contact-row {
    display: flex;
    align-items: center;
    gap: 8px;
    margin-top: 12px;
    font-size: 14px;
    color: var(--text-dark);
  }
  .contact-row + .contact-row { margin-top: 8px; }
  .contact-icon { width: 20px; height: 20px; flex: none; }

  /* Back */
  .card-back {
    left: 620px;
    background: linear-gradient(160deg, var(--brand-blue-deep) 0%, var(--brand-blue) 45%, var(--brand-blue-light) 100%);
  }
  .back-band {
    position: absolute;
    left: 0;
    top: 128px;
    width: 540px;
    height: 64px;
    background: var(--card-white);
  }
  .back-circle { position: absolute; left: 34px; top: 64px; }
  .company-name {
    position: absolute;
    left: 222px;
    top: 128px;
    height: 64px;
    display: flex;
    align-items: center;
    font-family: "Cinzel", serif;
    font-size: 16px;
    letter-spacing: 1px;
    white-space: nowrap;
    color: var(--brand-blue-deep);
    text-transform: uppercase;
  }
</style>
</head>
<body>

  <section class="card card-front" aria-label="Business card front">
    <svg class="front-circle" width="260" height="309" viewBox="0 0 260 309" aria-hidden="true">
      <defs>
        <radialGradient id="frontDisc" cx="40%" cy="35%" r="70%">
          <stop offset="0" stop-color="#3a7fd6"/>
          <stop offset="1" stop-color="#1a3f9c"/>
        </radialGradient>
      </defs>
      <circle cx="70" cy="250" r="176" fill="none" stroke="var(--ring-grey)" stroke-width="3"/>
      <circle cx="70" cy="250" r="168" fill="url(#frontDisc)"/>
    </svg>
    <div class="front-brand">Brimcove<br>Developers Corp</div>

    <div class="front-details">
      <h1 class="person-name">Darren Kopec</h1>
      <p class="person-title">OWNER</p>
      <p class="address">2917 NE 88th Avenue Suite 412<br>Coral Springs, FL 33071</p>
      <div class="contact-row">
        <svg class="contact-icon" viewBox="0 0 20 20" aria-hidden="true">
          <circle cx="10" cy="10" r="10" fill="var(--brand-blue)"/>
          <path d="M7 5.5c.6 0 1 .3 1.2.8l.5 1.4c.1.4 0 .8-.3 1l-.7.6c.5 1 1.3 1.8 2.3 2.3l.6-.7c.3-.3.7-.4 1-.3l1.4.5c.5.2.8.6.8 1.2v1c0 .7-.6 1.2-1.3 1.1C9 14 6 11 5.6 7.8 5.5 7.1 6 6.5 6.7 6.5z" fill="#fff"/>
        </svg>
        <span>(305) 555-0148</span>
      </div>
      <div class="contact-row">
        <svg class="contact-icon" viewBox="0 0 20 20" aria-hidden="true">
          <circle cx="10" cy="10" r="10" fill="var(--brand-blue)"/>
          <rect x="5" y="6.5" width="10" height="7" rx="1" fill="#fff"/>
          <path d="M5.5 7l4.5 3.5L14.5 7" fill="none" stroke="var(--brand-blue)" stroke-width="1"/>
        </svg>
        <span>darren@brimcovedev.example</span>
      </div>
    </div>
  </section>

  <section class="card card-back" aria-label="Business card back">
    <div class="back-band"></div>
    <svg class="back-circle" width="180" height="180" viewBox="0 0 180 180" aria-hidden="true">
      <defs>
        <radialGradient id="backDisc" cx="40%" cy="35%" r="70%">
          <stop offset="0" stop-color="#2f8fd0"/>
          <stop offset="1" stop-color="#1a3f9c"/>
        </radialGradient>
      </defs>
      <circle cx="90" cy="96" r="84" fill="#fff"/>
      <circle cx="90" cy="96" r="76" fill="none" stroke="#3a3a3a" stroke-width="2"/>
      <circle cx="90" cy="96" r="70" fill="url(#backDisc)"/>
    </svg>
    <div class="company-name">Brimcove Developers Corp</div>
  </section>

</body>
</html>
```